Basic / Quick Business Card

Quick easy design project!

Need a one sided basic business card that matches font & style of brand and bottle label for our gourmet condiment, Velvet Corwin Sauce. Velvet Corwin Sauce is sold in specialty retail, gourmet groceries and appears on chef-driven restaurant menus, so the target market is a high end, gourmet, artisan-made food-loving customer.

Files Included:
Sauce Bottle Label
Velvet Corwin Sauce Round Logos

**About the logos - the logo may be used in a circle or alone vertically as on side of the bottle label**

Layout of Card:
May be vertical or horizontal based on designer ideas.

Logo usage (in circle vs. stand alone vertical logo) is up to designers descretion as well.

Reverse side of business card will be various high end / professional product photos / food shots using us.zelk.com system. **Designer on this project will NOT design a reserve for the card.**

Paper that will be used for printing:
Zelk Classic - it's a WHITE paper, but we use a cream background on Velvet Corwin Sauce branding, so please take this into account on design to stay brand consistent.

Elements & Copy for Card:
1. Logo in either script horizontal or vertical version
2. Copy: "Artisan Made - Small Batch"
3. Name - Rory Whitlock
4. Title - Creator
5. Phone - xxx.xxx.xxxx
6. xxxx@velvetcorwin.com
7. URL: velvetcorwinsauce.com
8. Social Media: @getvelvetcorwin on Twitter / Facebook / Instagram

Please provide final files in Illustrator or InDesign format.

```html
<!DOCTYPE html>
<html lang="en">
<head>
<meta charset="utf-8">
<title>Velvet Corwin Sauce – Business Cards</title>
<link href="https://fonts.googleapis.com/css2?family=Bodoni+Moda:wght@400;500&display=swap" rel="stylesheet">
<style>
  :root {
    --page: #ffffff;
    --ink: #1e1b1a;
    --gold: #d9a627;
    --gold-light: #f7e3a6;
    --gold-deep: #b07d16;
    --cream: #f5f0dc;
    --white: #ffffff;
  }
  * { margin: 0; padding: 0; box-sizing: border-box; }
  html, body { width: 848px; height: 1200px; overflow: hidden; background: var(--page); }
  body { position: relative; font-family: "Bodoni Moda", "Times New Roman", serif; }

  .card {
    position: absolute;
    top: 215px;
    width: 387px;
    height: 674px;
    overflow: hidden;
    text-align: center;
  }
  .card--dark { left: 21px; background: var(--ink); border: 7px solid var(--gold); color: var(--white); }
  .card--gold {
    left: 444px;
    border: 7px solid var(--ink);
    color: var(--ink);
    background: radial-gradient(ellipse at 50% 55%, #fffbea 0%, #f6dd95 45%, var(--gold) 100%);
  }

  .corner-ribbons { position: absolute; inset: 0; width: 100%; height: 100%; pointer-events: none; }

  .line { position: absolute; left: 0; right: 0; line-height: 1; }
  .tagline { top: 26px; font-size: 15px; color: var(--white); }

  .seal {
    position: absolute;
    left: 50%;
    top: 96px;
    width: 244px;
    height: 244px;
    margin-left: -122px;
    border-radius: 50%;
    background: radial-gradient(circle at 40% 35%, var(--gold-light), var(--gold) 55%, var(--gold-deep));
  }
  .seal__disc {
    position: absolute;
    inset: 38px;
    border-radius: 50%;
    display: flex;
    align-items: center;
    justify-content: center;
    padding: 14px;
  }
  .card--dark .seal__disc { background: var(--cream); }
  .card--gold .seal__disc { background: var(--ink); }
  .brand-name { font-size: 25px; font-weight: 500; line-height: 1.15; }
  .card--dark .brand-name { color: var(--ink); }
  .card--gold .brand-name { color: var(--gold); }

  .person { top: 360px; font-size: 27px; }
  .role { top: 386px; font-size: 15px; }
  .phone { top: 496px; font-size: 20px; letter-spacing: 1px; }
  .email { top: 524px; font-size: 17px; }
  .site { top: 548px; font-size: 17px; }
  .handle { top: 601px; font-size: 10px; }
  .handle-on { top: 614px; font-size: 10px; }

  .social {
    position: absolute;
    top: 628px;
    left: 0; right: 0;
    display: flex;
    justify-content: center;
    gap: 4px;
  }
  .social__dot { width: 16px; height: 16px; border-radius: 50%; }
  .card--dark .social__dot { background: var(--white); }
  .card--gold .social__dot { background: var(--ink); }
</style>
</head>
<body>

<section class="card card--dark" aria-label="Business card, dark version">
  <svg class="corner-ribbons" viewBox="0 0 373 660" aria-hidden="true">
    <polygon points="300,0 325,0 373,48 373,73" fill="#e6b93f"/>
    <polygon points="0,587 0,612 48,660 73,660" fill="#e6b93f"/>
  </svg>
  <p class="line tagline">Artisan Made-Small Batch</p>
  <div class="seal" role="img" aria-label="Gold scalloped seal with ribbon framing the brand name">
    <div class="seal__disc"><span class="brand-name">Velvet Corwin Sauce</span></div>
  </div>
  <p class="line person">Rory Whitlock</p>
  <p class="line role">Creator</p>
  <p class="line phone">555-018-2477</p>
  <p class="line email">info@tastehollow.com</p>
  <p class="line site">www.velvetcorwinsauce.com</p>
  <p class="line handle">getvelvetcorwin</p>
  <p class="line handle-on">on</p>
  <div class="social" aria-label="Social networks">
    <span class="social__dot"></span><span class="social__dot"></span><span class="social__dot"></span>
  </div>
</section>

<section class="card card--gold" aria-label="Business card, gold version">
  <svg class="corner-ribbons" viewBox="0 0 373 660" aria-hidden="true">
    <polygon points="300,0 325,0 373,48 373,73" fill="#c8951f"/>
    <polygon points="0,587 0,612 48,660 73,660" fill="#c8951f"/>
  </svg>
  <p class="line tagline">Artisan Made-Small Batch</p>
  <div class="seal" role="img" aria-label="Gold scalloped seal with ribbon framing the brand name">
    <div class="seal__disc"><span class="brand-name">Velvet Corwin Sauce</span></div>
  </div>
  <p class="line person">Rory Whitlock</p>
  <p class="line role">Creator</p>
  <p class="line phone">555-018-2477</p>
  <p class="line email">info@tastehollow.com</p>
  <p class="line site">www.velvetcorwinsauce.com</p>
  <p class="line handle">getvelvetcorwin</p>
  <p class="line handle-on">on</p>
  <div class="social" aria-label="Social networks">
    <span class="social__dot"></span><span class="social__dot"></span><span class="social__dot"></span>
  </div>
</section>

</body>
</html>
```